KRT Design Business Card

I need to develop a business card for my real estate design and investment company. Something clean, classic and professional with a modern vibe.

Industry/Entity Type

Real Estate

Font styles to use
Serif
Sans Serif

```html
<!DOCTYPE html>
<html lang="en">
<head>
<meta charset="UTF-8">
<title>KRT Design Business Card</title>
<link href="https://fonts.googleapis.com/css2?family=Didact+Gothic&display=swap" rel="stylesheet">
<style>
  :root {
    --backdrop: #3b1613;
    --card-light: #ffffff;
    --card-dark: #363636;
    --ink: #2b2b2b;
    --ink-soft: #333333;
    --paper-text: #f4f4f4;
  }
  * { margin: 0; padding: 0; box-sizing: border-box; }
  html, body {
    width: 1200px;
    height: 1000px;
    overflow: hidden;
  }
  body {
    background: var(--backdrop);
    font-family: "Didact Gothic", "Century Gothic", sans-serif;
    position: relative;
  }
  .card {
    position: absolute;
    left: 265px;
    width: 666px;
    height: 398px;
    box-shadow: 0 6px 18px rgba(0,0,0,0.45);
  }
  .card--front { top: 73px; background: var(--card-light); color: var(--ink); }
  .card--back  { top: 532px; background: var(--card-dark); color: var(--paper-text); }

  .brand {
    position: absolute;
    display: flex;
    align-items: center;
    gap: 14px;
    font-weight: 400;
    white-space: nowrap;
  }
  .brand__mark {
    display: block;
    border: 2px solid currentColor;
  }
  .card--front .brand {
    left: 51px;
    top: 145px;
    font-size: 46px;
    color: var(--ink);
  }
  .card--front .brand__mark { width: 22px; height: 22px; }
  .card--back .brand {
    left: 0;
    right: 0;
    top: 165px;
    justify-content: center;
    font-size: 60px;
    color: var(--paper-text);
  }
  .card--back .brand__mark { width: 28px; height: 28px; }

  .contact {
    position: absolute;
    left: 374px;
    top: 122px;
  }
  .contact__name {
    font-size: 20px;
    line-height: 24px;
    color: var(--ink);
  }
  .contact__role {
    font-size: 14px;
    line-height: 18px;
    color: var(--ink-soft);
  }
  .contact__list {
    list-style: none;
    margin-top: 33px;
  }
  .contact__item {
    display: flex;
    align-items: center;
    gap: 6px;
    font-size: 15px;
    line-height: 19px;
    color: var(--ink);
  }
  .contact__icon {
    width: 11px;
    height: 11px;
    flex: none;
  }
</style>
</head>
<body>

  <section class="card card--front" aria-label="Business card front">
    <div class="brand">
      <span class="brand__mark" aria-hidden="true"></span>
      <span class="brand__name">KRT Design</span>
    </div>

    <div class="contact">
      <p class="contact__name">Daniel Reyes</p>
      <p class="contact__role">Founder</p>
      <ul class="contact__list">
        <li class="contact__item">
          <svg class="contact__icon" viewBox="0 0 12 12" aria-hidden="true"><rect x="3" y="0.5" width="6" height="11" rx="1" fill="none" stroke="#2b2b2b" stroke-width="1"/></svg>
          + 1 912 555 0142
        </li>
        <li class="contact__item">
          <svg class="contact__icon" viewBox="0 0 12 12" aria-hidden="true"><path d="M1 4 Q6 0 11 4 L9 5 L8 3.5 Q6 3 4 3.5 L3 5 Z" fill="#2b2b2b"/><rect x="2" y="6" width="8" height="5" rx="1" fill="#2b2b2b"/></svg>
          + 1 912 555 0187
        </li>
        <li class="contact__item">
          <svg class="contact__icon" viewBox="0 0 12 12" aria-hidden="true"><rect x="0.5" y="2.5" width="11" height="7" fill="#2b2b2b"/><path d="M0.5 2.5 L6 7 L11.5 2.5" fill="none" stroke="#fff" stroke-width="1"/></svg>
          info@krtdesignstudio.com
        </li>
        <li class="contact__item">
          <svg class="contact__icon" viewBox="0 0 12 12" aria-hidden="true"><circle cx="6" cy="6" r="5" fill="none" stroke="#2b2b2b" stroke-width="1.2"/><ellipse cx="6" cy="6" rx="2.2" ry="5" fill="none" stroke="#2b2b2b" stroke-width="1"/><line x1="1" y1="6" x2="11" y2="6" stroke="#2b2b2b" stroke-width="1"/></svg>
          www.krtdesignstudio.com
        </li>
      </ul>
    </div>
  </section>

  <section class="card card--back" aria-label="Business card back">
    <div class="brand">
      <span class="brand__mark" aria-hidden="true"></span>
      <span class="brand__name">KRT Design</span>
    </div>
  </section>

</body>
</html>
```